We currently have a good logo and we want business cards that can display our logo but also represent our industry - telecom construction - We are a construction company specializing in telecom construction such as installation of fiber optic cable throughout cities and across the country. Nationwide services
We are large enough to handle most any project yet small enough to be a flexible partner and resource.

Target Market(s)

U.S. based telecom carriers and providers

Industry/Entity Type

Construction

Contact Information for Business Card

Business cards should include our logo, phone number and website address. Also, including some information as to our core services would be good.

Colors

Designer to choose colors to be used in the design.

Requirements
Must have
• Colors based on logo
• Must use our logo
• Logo, name, email, website address, phone number
• Tovek Subterra
• Brent Dacosta
• Director of Business Development
• (913) 555-0187
• www.tovekgrid.example
Nice to have
• Construction services including:
• Small Cell Construction
• Boring/Drilling
• Plowing / Trenching
• Conduit installation
• Fiber pulling
• splicing
• building entries
• Aerial construction
• Aerial Make Ready
• Make Ready Engineering
Should not have
• We are open to ideas

```html
<!DOCTYPE html>
<html lang="en">
<head>
<meta charset="utf-8">
<title>Tovek Subterra – Business Card</title>
<link rel="stylesheet" href="https://fonts.googleapis.com/css2?family=Lato:wght@400;700;900&display=swap">
<style>
  :root {
    --brand-blue: #1654a8;
    --brand-blue-deep: #0f4596;
    --ink: #3d3f44;
    --muted-tint: #eef1f8;
    --card-white: #ffffff;
    --backdrop: #d9dbdf;
  }
  * { box-sizing: border-box; margin: 0; padding: 0; }
  html, body { width: 1200px; height: 900px; overflow: hidden; }
  body {
    background: var(--backdrop);
    font-family: "Lato", sans-serif;
    display: flex;
    flex-direction: column;
    align-items: center;
    justify-content: center;
    gap: 40px;
  }
  .card {
    width: 700px;
    height: 400px;
    border-radius: 22px;
    position: relative;
    overflow: hidden;
    box-shadow: 0 6px 18px rgba(0,0,0,0.18);
  }

  /* Back side */
  .card-back {
    background: var(--brand-blue);
    color: #fff;
    display: flex;
    flex-direction: column;
    align-items: center;
  }
  .card-back .brand-mark {
    margin-top: 92px;
    display: flex;
    align-items: center;
    gap: 14px;
    font-weight: 900;
    font-size: 50px;
    letter-spacing: 0.5px;
    color: #fff;
  }
  .card-back .brand-dot {
    width: 22px; height: 22px; border-radius: 50%;
    background: #fff;
  }
  .services {
    margin-top: 78px;
    text-align: center;
    font-size: 17px;
    line-height: 1.75;
    letter-spacing: 0.2px;
  }
  .services .sep { margin: 0 10px; }

  /* Front side */
  .card-front { background: var(--card-white); }
  .decor-fill {
    position: absolute;
    right: 0; top: 70px;
    width: 340px; height: 330px;
    background: var(--muted-tint);
    border-radius: 40px 0 0 0;
  }
  .card-front .brand-mark {
    position: absolute;
    right: 48px; top: 120px;
    display: flex;
    align-items: center;
    gap: 12px;
    font-weight: 900;
    font-size: 40px;
    color: var(--brand-blue);
  }
  .card-front .brand-square {
    width: 20px; height: 20px;
    background: var(--brand-blue);
  }
  .person {
    position: absolute;
    left: 52px; top: 72px;
  }
  .person-name {
    font-weight: 900;
    font-size: 40px;
    color: var(--brand-blue-deep);
  }
  .person-title {
    margin-top: 4px;
    font-size: 19px;
    color: var(--ink);
    letter-spacing: 0.3px;
  }
  .contact {
    position: absolute;
    left: 52px; bottom: 36px;
    font-size: 17px;
    color: var(--ink);
    line-height: 1.4;
  }
  .company { color: var(--brand-blue); }
  .address { margin-bottom: 10px; }
  .contact-row { display: flex; align-items: center; gap: 12px; }
  .contact-row svg { width: 18px; height: 18px; flex: none; }
  .accent { color: var(--brand-blue); }
</style>
</head>
<body>

  <section class="card card-back">
    <div class="brand-mark"><span class="brand-dot"></span>Tovek Subterra</div>
    <div class="services">
      <div>Small Cell Construction<span class="sep">•</span>Boring/Drilling<span class="sep">•</span>Plowing / Trenching</div>
      <div>Conduit installation<span class="sep">•</span>Fiber pulling<span class="sep">•</span>Building entries<span class="sep">•</span>Aerial construction</div>
      <div>Splicing<span class="sep">•</span>Aerial Make Ready<span class="sep">•</span>Make Ready Engineering</div>
    </div>
  </section>

  <section class="card card-front">
    <div class="decor-fill" role="img" aria-label="Faint large drill bit decoration in pale blue"></div>
    <div class="brand-mark"><span class="brand-square"></span>Tovek Subterra</div>

    <div class="person">
      <div class="person-name">Brent Dacosta</div>
      <div class="person-title">Director of Business Development</div>
    </div>

    <div class="contact">
      <div class="company">Tovek Subterra</div>
      <div class="address">48 Harlow Street Kansas City,<br>KS 66190</div>
      <div class="contact-row">
        <svg viewBox="0 0 24 24" aria-hidden="true"><path fill="#1654a8" d="M6.6 10.8a15 15 0 0 0 6.6 6.6l2.2-2.2a1 1 0 0 1 1-.25 11.4 11.4 0 0 0 3.6.57 1 1 0 0 1 1 1V20a1 1 0 0 1-1 1A17 17 0 0 1 3 4a1 1 0 0 1 1-1h3.5a1 1 0 0 1 1 1c0 1.25.2 2.45.57 3.57a1 1 0 0 1-.25 1z"/></svg>
        <span>(913) 555-0187</span>
      </div>
      <div class="contact-row">
        <svg viewBox="0 0 24 24" aria-hidden="true"><rect x="2" y="5" width="20" height="14" rx="1.5" fill="#1654a8"/><path d="M3 6l9 7 9-7" fill="none" stroke="#fff" stroke-width="1.6"/></svg>
        <span>brent.dacosta@tovekgrid.example</span>
      </div>
      <div class="contact-row">
        <svg viewBox="0 0 24 24" aria-hidden="true"><circle cx="12" cy="12" r="9.5" fill="none" stroke="#1654a8" stroke-width="1.8"/><ellipse cx="12" cy="12" rx="4" ry="9.5" fill="none" stroke="#1654a8" stroke-width="1.5"/><path d="M2.5 12h19M4 7.5h16M4 16.5h16" stroke="#1654a8" stroke-width="1.4"/></svg>
        <span>www.<span class="accent">tovekgrid</span>.example</span>
      </div>
    </div>
  </section>

</body>
</html>
```